Meadowlark Soaps Business Card

The new business card design will incorporate my new logo components designed by one of your designers. Meadowlark Soaps creates high quality soaps and bath products. They would be suited for a Spa, Bed and Breakfast, Boutique environment. The look should be a white background.
Classy, soft and using the colour palet of the logo. The card will be two sided.

Reason: Need more time to make some changes and decide.

Target Market(s)

Looking to appeal to an upper end market. Spas, boutiques, independent gift stores, bridal salons, bed and breakfast, etc. I want the card to impart a sense of elegance, tranquility and Meadowlark. But also quality and value.

Industry/Entity Type

Business

Font styles to use
Sans Serif
Script

Requirements
Must have
• My logo on the front. But also on the back but faded out to allow written notes on the back.
On the front : Marta Quennell
Owner/Creator
47 Ashcombe Rd
Guelph, Ont K7R 2M5
555.014.2938
Creating Quality Handcrafted Soaps And Bath Products
Custom and Wholesale Orders Welcome
Www.meadowlarksoaps.ca
Www.facebook.com / MeadowlarkSoapandBath
info@meadowlarksoaps.ca

```html
<!DOCTYPE html>
<html lang="en">
<head>
<meta charset="utf-8">
<title>Meadowlark Soaps Business Card</title>
<link rel="stylesheet" href="https://fonts.googleapis.com/css2?family=Lato:wght@400;700&family=Pinyon+Script&display=swap">
<style>
  :root {
    --bg: #2e2e2e;
    --card: #fbfbfa;
    --teal: #6fa393;
    --teal-soft: #a9cbbf;
    --teal-faint: #e3ede9;
    --ink: #555a58;
    --ink-dark: #3d3f3e;
  }
  * { margin: 0; padding: 0; box-sizing: border-box; }
  html, body { width: 1200px; height: 997px; overflow: hidden; }
  body {
    background: var(--bg);
    font-family: "Lato", Arial, sans-serif;
    color: var(--ink);
    position: relative;
  }
  .card {
    position: absolute;
    width: 700px;
    height: 400px;
    left: 250px;
    background: var(--card);
    border-radius: 26px;
    box-shadow: 0 14px 40px rgba(0,0,0,.45);
    overflow: hidden;
  }
  .card--back { top: 48px; }
  .card--front { top: 520px; }

  /* back */
  .faded-brand {
    position: absolute; z-index: 0; white-space: nowrap;
    font-weight: 400; color: var(--teal-faint);
    display: flex; align-items: center; gap: 10px;
  }
  .faded-brand--left { left: 36px; top: 150px; font-size: 28px; }
  .faded-brand--center { left: 250px; top: 250px; font-size: 42px; }
  .brand-dot { display: inline-block; border-radius: 50%; background: currentColor; flex: none; }
  .faded-brand--left .brand-dot { width: 18px; height: 18px; }
  .faded-brand--center .brand-dot { width: 26px; height: 26px; }
  .notes-title {
    position: absolute; z-index: 1; left: 290px; top: 58px;
    font-weight: 700; font-size: 22px; color: var(--ink-dark);
    text-decoration: underline; text-underline-offset: 4px;
  }
  .notes-lines { position: absolute; z-index: 1; left: 140px; top: 110px; width: 500px; }
  .notes-line { border-bottom: 4px dotted var(--teal-soft); height: 62px; }

  /* front */
  .brand {
    position: absolute; right: 50px; top: 58px; white-space: nowrap;
    display: flex; align-items: center; gap: 12px;
    color: var(--teal); font-weight: 400; font-size: 32px;
  }
  .brand .brand-dot { width: 38px; height: 38px; }
  .person { position: absolute; left: 50px; top: 112px; }
  .person-name {
    font-family: "Pinyon Script", cursive; font-size: 44px;
    color: var(--teal); line-height: 1; white-space: nowrap;
  }
  .person-role { font-size: 13px; letter-spacing: 1px; color: var(--ink); margin: 4px 0 0 36px; }
  .rule { position: absolute; left: 40px; right: 36px; height: 3px; background: var(--teal); }
  .rule--top { top: 180px; left: 330px; }
  .rule--mid { top: 270px; }
  .contact { position: absolute; list-style: none; font-size: 15px; color: var(--ink); white-space: nowrap; }
  .contact li { display: flex; align-items: center; gap: 10px; height: 28px; }
  .contact svg { width: 16px; height: 16px; fill: var(--teal); flex: none; }
  .contact--right { left: 330px; top: 200px; }
  .contact--left { left: 50px; top: 282px; }
  .tagline {
    position: absolute; left: 0; right: 0; bottom: 16px;
    text-align: center; font-weight: 700; font-size: 17px; color: var(--teal);
  }
</style>
</head>
<body>

<section class="card card--back" aria-label="Card back, notes side">
  <div class="faded-brand faded-brand--left"><span class="brand-dot"></span>Meadowlark Soaps</div>
  <div class="faded-brand faded-brand--center"><span class="brand-dot"></span>Meadowlark Soaps</div>
  <h2 class="notes-title">Notes</h2>
  <div class="notes-lines">
    <div class="notes-line"></div>
    <div class="notes-line"></div>
    <div class="notes-line"></div>
    <div class="notes-line"></div>
  </div>
</section>

<section class="card card--front" aria-label="Card front">
  <div class="brand"><span class="brand-dot"></span>Meadowlark Soaps</div>
  <div class="person">
    <p class="person-name">Marta Quennell</p>
    <p class="person-role">OWNER/CREATOR</p>
  </div>
  <div class="rule rule--top"></div>
  <ul class="contact contact--right">
    <li><svg viewBox="0 0 20 20"><circle cx="10" cy="10" r="8"/></svg>facebook.com/MeadowlarkSoapandBath</li>
    <li><svg viewBox="0 0 20 20"><path d="M10 1a6.5 6.5 0 0 0-6.5 6.5C3.5 12.5 10 19 10 19s6.5-6.5 6.5-11.5A6.5 6.5 0 0 0 10 1zm0 9a2.5 2.5 0 1 1 0-5 2.5 2.5 0 0 1 0 5z"/></svg>47 Ashcombe Rd, Guelph, Ont K7R 2M5</li>
  </ul>
  <div class="rule rule--mid"></div>
  <ul class="contact contact--left">
    <li><svg viewBox="0 0 20 20"><path d="M2 6c0-2 2-3 8-3s8 1 8 3v2h-4V6H6v2H2zM5 9h10l2 8H3z"/></svg>555.014.2938</li>
    <li><svg viewBox="0 0 20 20"><path d="M8.5 11.5l3-3M7 9l-2 2a3 3 0 0 0 4 4l2-2M13 11l2-2a3 3 0 0 0-4-4L9 7" stroke="#6fa393" stroke-width="2" fill="none"/></svg>www.meadowlarksoaps.ca</li>
  </ul>
  <p class="tagline">Creating quality handcrafted Soaps &amp; Bath Products</p>
</section>

</body>
</html>
```